Kelton Produce and Landscape Supplies

We require a design for a new business. It is a multi purpose business that supplies Animal foods and supplies for farmers as well as for pets focusing on horses. We also provide landscape materials, Gravels, Sands, Soils, mulches, garden furniture, water features, statues etc. Attached to the business is a new cafe called the "Mapleview Cafe". We have a small gift shop, post office and general store on the premises. To add to the challenge we have farmyard animals like goats, pigs, chickens, ducks, cows, miniature horse along with rabbits, dogs, cats, snakes and birds. I would like to market the total business over both sides of the flyer. Perhaps the Produce and Landscape Supplies on one side and the Cafe and gifts shop etc on the reverse? I have attached a entrance sign that we recently had designed. The Cow is going to be our main character as we are located in dairy farm country.

Industry/Entity Type

Business

```html
<!DOCTYPE html>
<html lang="en">
<head>
<meta charset="utf-8">
<title>Kelton Produce and Landscape Supplies – Flyer</title>
<link rel="stylesheet" href="https://fonts.googleapis.com/css2?family=Special+Elite&family=Open+Sans:wght@400;600;700&family=PT+Sans+Narrow:wght@400;700&display=swap">
<style>
  :root {
    --green: #7dba3c;
    --green-light: #9ccd5c;
    --green-dark: #1f6a36;
    --white: #ffffff;
    --ink: #1a1a1a;
    --backdrop: #e9e7e2;
    --photo-garden: #5f8a3e;
    --photo-gravel: #9c9ea6;
    --photo-mulch: #6b3a24;
    --photo-wood: #8a6a45;
    --photo-sky: #6f9fd8;
    --photo-shed: #d9cfae;
    --mascot: #bfe0ec;
    --barn: #c8463c;
    --map: #efeee9;
  }
  * { margin: 0; padding: 0; box-sizing: border-box; }
  html, body { width: 1200px; height: 868px; overflow: hidden; background: var(--backdrop); }
  .canvas { position: relative; width: 1200px; height: 868px; }
  .flyer {
    position: absolute; top: 52px; width: 540px; height: 764px;
    background: var(--white); overflow: hidden;
    box-shadow: 0 4px 14px rgba(0,0,0,.22);
    font-family: "Open Sans", sans-serif;
  }
  .flyer--produce { left: 40px; }
  .flyer--cafe { left: 620px; }
  .flyer__art { position: absolute; inset: 0; width: 540px; height: 764px; }
  .title {
    position: absolute; font-family: "Special Elite", monospace;
    color: var(--ink); letter-spacing: 1px; line-height: 1.12;
  }
  .flyer--produce .title { left: 22px; top: 350px; font-size: 23px; }
  .flyer--cafe .title { left: 22px; top: 277px; font-size: 31px; letter-spacing: 2px; }
  .pill {
    position: absolute; background: var(--green-dark); color: var(--white);
    font-weight: 700; border-radius: 14px; text-align: center;
  }
  .pill--products { left: 22px; top: 464px; width: 166px; height: 27px; font-size: 16px; line-height: 27px; letter-spacing: .5px; }
  .pill--coffee { left: 79px; top: 440px; width: 382px; height: 30px; font-size: 16px; line-height: 30px; }
  .product-list { position: absolute; left: 25px; top: 508px; list-style: none; }
  .product-list li {
    color: var(--white); font-size: 17.5px; font-weight: 600;
    height: 28px; line-height: 28px; display: flex; align-items: center; gap: 6px;
  }
  .product-list svg { width: 13px; height: 13px; flex: none; }
  .animal-box {
    position: absolute; left: 305px; top: 522px; width: 250px; height: 112px;
    background: var(--white); border-radius: 8px 0 0 8px;
    box-shadow: 0 2px 6px rgba(0,0,0,.25);
  }
  .animal-box__frame { position: absolute; inset: 6px; border: 1.5px dotted #555; border-radius: 5px; }
  .animal-box__art { position: absolute; left: 60px; top: 6px; width: 120px; height: 50px; border-radius: 6px;
    background: linear-gradient(90deg, #6e5a45, #c8a07a 50%, #3b3b3b); }
  .animal-box__label { position: absolute; left: 8px; top: 60px; width: 230px; text-align: center;
    color: var(--green-dark); font-family: "PT Sans Narrow", sans-serif; font-weight: 700; font-size: 18px; line-height: 20px; }
  .phone {
    position: absolute; display: flex; align-items: center; gap: 6px;
    color: var(--green-dark); font-weight: 700;
  }
  .phone svg { flex: none; }
  .flyer--produce .phone { left: 343px; top: 688px; font-size: 20px; }
  .address-bar {
    position: absolute; left: 28px; width: 500px; height: 28px; border-radius: 14px;
    background: var(--green); color: var(--ink); font-size: 14px; letter-spacing: .6px;
    display: flex; align-items: center; justify-content: center; gap: 8px;
    box-shadow: 0 2px 3px rgba(0,0,0,.25);
  }
  .flyer--produce .address-bar { top: 728px; }
  .flyer--cafe .address-bar { top: 728px; left: 22px; width: 498px; }
  .subtitle { position: absolute; left: 20px; top: 374px; color: var(--white); font-weight: 700; font-size: 22px; }
  .about {
    position: absolute; left: 30px; top: 481px; width: 480px; text-align: center;
    color: var(--white); font-family: "PT Sans Narrow", sans-serif; font-size: 16.5px; line-height: 20px;
  }
  .venue-photo { position: absolute; left: 19px; top: 603px; width: 143px; height: 82px;
    background: linear-gradient(180deg, var(--photo-sky) 0 45%, var(--photo-shed) 45% 80%, #8a8a80 80%); }
  .venue-caption { position: absolute; left: 19px; top: 686px; width: 150px; font-size: 10px; line-height: 12px; color: var(--ink); letter-spacing: .3px; }
  .hours { position: absolute; left: 165px; top: 633px; width: 120px; text-align: center;
    font-family: "PT Sans Narrow", sans-serif; color: var(--green-dark); font-size: 11.5px; line-height: 16px; }
  .hours__title { font-weight: 700; font-size: 12px; }
  .flyer--cafe .phone { left: 178px; top: 690px; font-size: 13px; }
  .map { position: absolute; left: 294px; top: 571px; width: 240px; height: 135px; border-radius: 8px; background: var(--map); }
</style>
</head>
<body>
<main class="canvas">

  <!-- Produce & landscape side -->
  <article class="flyer flyer--produce">
    <svg class="flyer__art" viewBox="0 0 540 764" aria-hidden="false">
      <defs>
        <linearGradient id="gardenTone" x1="0" y1="0" x2="0" y2="1">
          <stop offset="0" stop-color="#3f6e2e"/><stop offset=".6" stop-color="#6f9a48"/><stop offset="1" stop-color="#9c9ea6"/>
        </linearGradient>
      </defs>
      <rect role="img" aria-label="Photo of a landscaped garden with stone steps, gravel and conifers" x="0" y="0" width="540" height="340" fill="url(#gardenTone)"/>
      <path d="M0,332 C160,312 360,318 540,262 L540,764 L0,764 Z" fill="var(--white)"/>
      <path d="M0,418 C170,438 360,430 540,380 L540,642 C380,650 190,680 0,708 Z" fill="var(--green)"/>
      <path d="M0,700 C200,672 380,650 540,636 L540,646 C380,660 200,684 0,712 Z" fill="var(--green-dark)"/>
      <path d="M0,692 C200,664 380,642 540,628" stroke="var(--green-dark)" stroke-width="1.5" fill="none"/>
      <circle cx="94" cy="265" r="82" fill="rgba(255,255,255,.55)"/>
      <circle role="img" aria-label="Cow mascot illustration" cx="94" cy="265" r="72" fill="var(--mascot)" stroke="#7a7a7a" stroke-width="5"/>
      <circle cx="340" cy="447" r="70" fill="rgba(255,255,255,.45)"/>
      <circle role="img" aria-label="Photo of red bark mulch" cx="340" cy="447" r="62" fill="var(--photo-mulch)"/>
      <circle cx="473" cy="434" r="70" fill="rgba(255,255,255,.45)"/>
      <circle role="img" aria-label="Photo of grey gravel" cx="473" cy="434" r="62" fill="var(--photo-gravel)"/>
      <circle cx="395" cy="356" r="80" fill="rgba(255,255,255,.6)"/>
      <circle role="img" aria-label="Photo of wicker garden furniture" cx="395" cy="356" r="70" fill="var(--photo-wood)"/>
    </svg>

    <h1 class="title">KELTON PRODUCE AND<br>LANDSCAPE SUPPLIES</h1>

    <div class="pill pill--products">OUR PRODUCTS</div>
    <ul class="product-list">
      <li><svg viewBox="0 0 14 14"><circle cx="7" cy="7" r="7" fill="var(--green-dark)"/><path d="M3.6,7.2 L6,9.5 L10.4,4.8" stroke="#fff" stroke-width="1.8" fill="none"/></svg>Landscape Materials</li>
      <li><svg viewBox="0 0 14 14"><circle cx="7" cy="7" r="7" fill="var(--green-dark)"/><path d="M3.6,7.2 L6,9.5 L10.4,4.8" stroke="#fff" stroke-width="1.8" fill="none"/></svg>Gravels, Sands, Soils</li>
      <li><svg viewBox="0 0 14 14"><circle cx="7" cy="7" r="7" fill="var(--green-dark)"/><path d="M3.6,7.2 L6,9.5 L10.4,4.8" stroke="#fff" stroke-width="1.8" fill="none"/></svg>Mulches</li>
      <li><svg viewBox="0 0 14 14"><circle cx="7" cy="7" r="7" fill="var(--green-dark)"/><path d="M3.6,7.2 L6,9.5 L10.4,4.8" stroke="#fff" stroke-width="1.8" fill="none"/></svg>Garden Furniture</li>
      <li><svg viewBox="0 0 14 14"><circle cx="7" cy="7" r="7" fill="var(--green-dark)"/><path d="M3.6,7.2 L6,9.5 L10.4,4.8" stroke="#fff" stroke-width="1.8" fill="none"/></svg>Water Features</li>
      <li><svg viewBox="0 0 14 14"><circle cx="7" cy="7" r="7" fill="var(--green-dark)"/><path d="M3.6,7.2 L6,9.5 L10.4,4.8" stroke="#fff" stroke-width="1.8" fill="none"/></svg>Statues</li>
    </ul>

    <div class="animal-box">
      <div class="animal-box__frame"></div>
      <div class="animal-box__art" role="img" aria-label="Group of farm animals: cow, horse, sheep, goat and chickens"></div>
      <p class="animal-box__label">ANIMAL FOODS &amp; SUPPLIES<br>FOR FARMERS</p>
    </div>

    <p class="phone">
      <svg width="22" height="22" viewBox="0 0 24 24"><circle cx="12" cy="12" r="10.5" fill="none" stroke="var(--green-dark)" stroke-width="2"/><path d="M8.3,6.5 L10,6.3 L11,9 L9.8,10 C10.5,11.7 12,13.2 13.7,14 L14.8,12.9 L17.4,14 L17.2,15.8 C14,17 7,10.5 8.3,6.5 Z" fill="var(--green-dark)"/></svg>
      61 2 5550 0148
    </p>

    <p class="address-bar">
      <svg width="12" height="16" viewBox="0 0 12 16"><path d="M6,0 C2.7,0 0,2.6 0,5.8 C0,10 6,16 6,16 C6,16 12,10 12,5.8 C12,2.6 9.3,0 6,0 Z" fill="var(--ink)"/><circle cx="6" cy="5.8" r="2.2" fill="var(--green)"/></svg>
      412 Brindle Creek Road Kelton, New South Wales
    </p>
  </article>

  <!-- Cafe side -->
  <article class="flyer flyer--cafe">
    <svg class="flyer__art" viewBox="0 0 540 764">
      <defs>
        <linearGradient id="shopTone" x1="0" y1="0" x2="0" y2="1">
          <stop offset="0" stop-color="#5f95d6"/><stop offset=".35" stop-color="#8db6e0"/><stop offset=".45" stop-color="#5a5348"/><stop offset=".6" stop-color="#ddd3b2"/><stop offset="1" stop-color="#9a9a92"/>
        </linearGradient>
      </defs>
      <rect role="img" aria-label="Photo of the produce store building with open-now flags" x="0" y="0" width="540" height="250" fill="url(#shopTone)"/>
      <path d="M0,258 C200,238 380,240 540,200 L540,764 L0,764 Z" fill="var(--white)"/>
      <path d="M0,338 C180,322 380,328 540,300 L540,540 C380,560 200,580 0,590 Z" fill="var(--green)"/>
      <path d="M0,580 C200,570 380,550 540,530 L540,542 C380,562 200,582 0,592 Z" fill="var(--green-dark)"/>
      <circle cx="93" cy="181" r="82" fill="rgba(255,255,255,.55)"/>
      <circle role="img" aria-label="Cow mascot illustration" cx="93" cy="181" r="72" fill="var(--mascot)" stroke="#7a7a7a" stroke-width="5"/>
      <circle cx="339" cy="363" r="70" fill="rgba(255,255,255,.45)"/>
      <circle role="img" aria-label="Photo of the cafe entrance with cafe flags" cx="339" cy="363" r="62" fill="#6b8fb8"/>
      <circle cx="471" cy="331" r="70" fill="rgba(255,255,255,.45)"/>
      <circle role="img" aria-label="Photo of the cafe coffee machine and counter" cx="471" cy="331" r="62" fill="#7a6a58"/>
      <circle cx="398" cy="263" r="78" fill="rgba(255,255,255,.6)"/>
      <circle cx="398" cy="263" r="68" fill="var(--white)"/>
      <circle role="img" aria-label="Illustration of a red barn and silo" cx="398" cy="263" r="48" fill="var(--barn)" opacity=".85"/>
    </svg>

    <h2 class="title">MAPLEVIEW CAFE</h2>
    <p class="subtitle">CAFE AND GIFTS SHOP</p>
    <div class="pill pill--coffee">TAKE A BREAK WITH FRESH COFFEE!</div>
    <p class="about">Kelton Produce is located in Kelton, NSW. We supply farm produce supplies, pet products, landscape supplies, a post office, a cafe and giftware.</p>

    <div class="venue-photo" role="img" aria-label="Photo of the store front"></div>
    <p class="venue-caption">412 Brindle Creek Road Kelton, New South Wales</p>

    <div class="hours">
      <p class="hours__title">OPENING HOURS</p>
      <p>Monday - Friday 7.30am - 5pm</p>
      <p>Saturday 8am - 12noon</p>
    </div>

    <p class="phone">
      <svg width="16" height="16" viewBox="0 0 24 24"><circle cx="12" cy="12" r="10.5" fill="none" stroke="var(--green-dark)" stroke-width="2"/><path d="M8.3,6.5 L10,6.3 L11,9 L9.8,10 C10.5,11.7 12,13.2 13.7,14 L14.8,12.9 L17.4,14 L17.2,15.8 C14,17 7,10.5 8.3,6.5 Z" fill="var(--green-dark)"/></svg>
      61 2 5550 0148
    </p>

    <div class="map" role="img" aria-label="Street map showing the store location"></div>

    <p class="address-bar">
      <svg width="12" height="16" viewBox="0 0 12 16"><path d="M6,0 C2.7,0 0,2.6 0,5.8 C0,10 6,16 6,16 C6,16 12,10 12,5.8 C12,2.6 9.3,0 6,0 Z" fill="var(--ink)"/><circle cx="6" cy="5.8" r="2.2" fill="var(--green)"/></svg>
      412 Brindle Creek Road Kelton, New South Wales
    </p>
  </article>

</main>
</body>
</html>
```